Medical equipment business looking for professional, unique business card

We need a business card design for a durable medical equipment company. We are small but would like our cards to express that we are much bigger. We focus on braces (back, knee, wrist, etc) but also do crutches, rollators, wheelchairs- basically medical equipment that gets you going and back in Action. Our colors are blue and green and our logo has an arrow and use of a "spine". We'd like to express professionalism while being unique.

Industry/Entity Type

Medical Equipment

Contact Information for Business Card

Professional feel but unique. Memorable.

Font styles to use
Serif
Sans Serif
Other font styles liked:
• verdana

Requirements
Must have
• card holders cell#, business phone#, fax#, email, website address, business address, logo
Nice to have
• use of medical/healthcare related descriptive words, items, look
Should not have
• the wrong colors or cartoon characters.

```html
<!DOCTYPE html>
<html lang="en">
<head>
<meta charset="utf-8">
<title>Kinetic DME – Business Card</title>
<link href="https://fonts.googleapis.com/css2?family=Exo+2:wght@600&family=Roboto:wght@400;500&display=swap" rel="stylesheet">
<style>
  :root {
    --backdrop: #e6e6e6;
    --card-white: #f7f7f7;
    --navy: #003f66;
    --green: #7ab929;
    --text-light: #ffffff;
    --card-shadow: 0 3px 6px rgba(0,0,0,0.25);
  }
  * { margin: 0; padding: 0; box-sizing: border-box; }
  html, body {
    width: 1200px; height: 576px; overflow: hidden;
    background: var(--backdrop);
    font-family: "Roboto", Arial, sans-serif;
  }
  .canvas { position: relative; width: 1200px; height: 576px; }

  .card {
    position: absolute; top: 138px; height: 294px;
    border-radius: 7px; overflow: hidden;
    background: var(--card-white);
    box-shadow: var(--card-shadow);
  }
  .card-front { left: 82px; width: 485px; }
  .card-back { left: 602px; width: 480px; }

  .brand {
    display: flex; align-items: center; gap: 10px;
    color: var(--navy);
    font-family: "Roboto", Arial, sans-serif;
    font-weight: 500;
    white-space: nowrap;
  }
  .brand-dot { border-radius: 50%; background: var(--green); flex: none; }

  .card-front .brand {
    position: absolute; left: 50%; top: 50%;
    transform: translate(-50%, -50%);
    font-size: 40px;
  }
  .card-front .brand-dot { width: 18px; height: 18px; }

  .card-back .brand {
    position: absolute; left: 78px; top: 148px;
    transform: translate(-50%, -50%) rotate(-90deg);
    font-size: 30px;
  }
  .card-back .brand-dot { width: 14px; height: 14px; }

  .back-panel { position: absolute; inset: 0; width: 480px; height: 294px; }

  .holder {
    position: absolute; right: 25px; top: 22px;
    text-align: right; color: var(--text-light);
  }
  .holder-name {
    font-family: "Exo 2", Arial, sans-serif; font-weight: 600;
    font-size: 19px; letter-spacing: 0.5px; line-height: 1.2;
  }
  .holder-title { font-size: 12px; margin-top: 2px; }

  .address {
    position: absolute; right: 25px; top: 166px;
    text-align: right; color: var(--text-light);
    font-size: 12.5px; line-height: 18px;
  }
  .contacts {
    position: absolute; right: 25px; top: 211px;
    list-style: none; color: var(--text-light);
    font-size: 12.5px; line-height: 18px;
  }
  .contacts li { display: flex; justify-content: flex-end; align-items: center; gap: 6px; }
  .contacts svg { width: 11px; height: 11px; fill: var(--text-light); flex: none; }
</style>
</head>
<body>
<main class="canvas">

  <section class="card card-front" aria-label="Card front">
    <div class="brand"><span class="brand-dot"></span>Kinetic DME</div>
  </section>

  <section class="card card-back" aria-label="Card back">
    <svg class="back-panel" viewBox="0 0 480 294" preserveAspectRatio="none" aria-hidden="true">
      <path d="M160 0 C 182 70, 192 150, 172 220 C 164 250, 154 275, 146 294 L 480 294 L 480 0 Z" fill="var(--green)"/>
      <path d="M166 0 C 188 70, 198 150, 178 220 C 170 250, 160 275, 153 294 L 480 294 L 480 0 Z" fill="var(--navy)"/>
    </svg>

    <div class="brand"><span class="brand-dot"></span>Kinetic DME</div>

    <div class="holder">
      <p class="holder-name">Daniel Reyes</p>
      <p class="holder-title">Managing Director</p>
    </div>

    <address class="address" style="font-style:normal">
      4120 Harbor Lane No.45<br>
      Glendale California 90000
    </address>

    <ul class="contacts">
      <li>+111 555 0142
        <svg viewBox="0 0 12 12" aria-label="Mobile"><path d="M3 0h6a1 1 0 0 1 1 1v10a1 1 0 0 1-1 1H3a1 1 0 0 1-1-1V1a1 1 0 0 1 1-1zm0 1.5v8h6v-8zm3 8.7a.7.7 0 1 0 0 1.4.7.7 0 0 0 0-1.4z"/></svg>
      </li>
      <li>www.kineticdme.com
        <svg viewBox="0 0 12 12" aria-label="Telephone"><path d="M1 4c0-2 2-3 5-3s5 1 5 3v1H8.5V3.8H3.5V5H1zM3 6h6l2 4v1H1v-1zm3 1.3a1.5 1.5 0 1 0 0 3 1.5 1.5 0 0 0 0-3z"/></svg>
      </li>
      <li>daniel@kineticdme.com
        <svg viewBox="0 0 12 12" aria-label="Email"><path d="M0 2h12v8H0zm1 1v.3l5 3.4 5-3.4V3zm0 1.5V9h10V4.5L6 8z"/></svg>
      </li>
    </ul>
  </section>

</main>
</body>
</html>
```